modernized upgrade to existing squarespace site

Hello! I have the following page for my consulting firm: https://hollinbrookcounsel.com/ Would love to upgrade to something more modern/attractive like here: https://www.pemberlowgroup.com/ or https://brightquillstudio.com/ , but I am open to creativity. Would like to retain the logo look and color theme from the logo. The rest can be left to creative discretion.

```html
<!DOCTYPE html>
<html lang="en">
<head>
<meta charset="utf-8">
<title>Hollinbrook Counsel</title>
<link href="https://fonts.googleapis.com/css2?family=Cinzel:wght@400;500&family=Figtree:wght@400;500;600&display=swap" rel="stylesheet">
<style>
:root{
  --rose:#d6b4b7;
  --rose-line:#d9aeb1;
  --rose-text:#d39ea3;
  --ink:#151515;
  --body:#4a4a4a;
  --footer:#f4f3f3;
  --white:#ffffff;
}
*{margin:0;padding:0;box-sizing:border-box}
html,body{width:1200px;height:2826px;overflow:hidden;background:var(--white)}
body{position:relative;font-family:"Figtree",Arial,sans-serif;color:var(--ink)}
.abs{position:absolute}
.serif{font-family:"Cinzel",Georgia,serif;font-weight:400}

/* hero */
.hero{left:0;top:0;width:1200px;height:560px;
  background:linear-gradient(180deg,#8ea1b4 0%,#b3a9b0 22%,#c79d8f 40%,#6c625f 62%,#3b3a3d 100%)}
.hero-shade{left:0;top:0;width:1200px;height:560px;
  background:linear-gradient(90deg,rgba(30,30,35,.35),rgba(0,0,0,0) 60%)}
.brand{left:145px;top:18px;display:flex;align-items:center;gap:10px}
.brand-square{width:40px;height:40px;border:2px solid #333}
.brand-name{font-family:"Cinzel",Georgia,serif;font-size:19px;letter-spacing:1.5px;color:#222;line-height:1}
.nav{left:352px;top:30px;display:flex;gap:20px;font-size:14px;color:#111}
.nav .active{text-decoration:underline;text-underline-offset:4px}
.btn-outline{left:927px;top:18px;width:128px;height:40px;border:2px solid #111;
  font-size:14px;font-weight:500;display:flex;align-items:center;justify-content:center}
.hero-frame{left:784px;top:126px;width:244px;height:200px;border:6px solid rgba(214,170,170,.55)}
.hero-title{left:143px;top:402px;font-size:41px;color:var(--white);letter-spacing:1px}
.hero-sub{left:143px;top:466px;font-size:16px;font-weight:600;color:var(--white)}

/* sections */
.h2{font-family:"Cinzel",Georgia,serif;font-weight:400;font-size:33px;letter-spacing:1.5px;text-align:center;width:1200px;left:0}
.para{font-size:13.5px;line-height:24px;color:var(--body)}
.center{text-align:center}
.btn-rose{background:var(--rose);width:133px;height:40px;font-size:14px;font-weight:500;
  display:flex;align-items:center;justify-content:center;color:#222}
.btn-dark{background:#151515;color:var(--white);width:133px;height:40px;font-size:14px;font-weight:500;
  display:flex;align-items:center;justify-content:center}
.line{border:2px solid var(--rose-line)}
.feature-title{font-family:"Cinzel",Georgia,serif;font-size:25px;line-height:36px;letter-spacing:1.3px}
.photo{position:absolute}

/* services */
.services{left:0;top:1728px;width:1200px;height:397px;background:var(--rose)}
.service{width:240px;text-align:center;font-size:17px;color:#1d1d1d}
.service svg{display:block;margin:0 auto 16px}

/* news */
.card{width:216px;text-align:center}
.card .thumb{height:160px}
.card h3{font-weight:400;font-size:16px;line-height:26px;margin-top:16px;color:#222;height:52px}
.card a{display:inline-block;margin-top:2px;font-size:14px;color:var(--rose-text);text-decoration:underline}

/* footer */
.footer{left:0;top:2580px;width:1200px;height:200px;background:var(--footer)}
.footer-links{font-size:13px;line-height:24px;color:#333}
.copy{left:0;top:2796px;width:1200px;text-align:center;font-size:12.5px;color:#222}
</style>
</head>
<body>

<!-- hero -->
<div class="abs hero" role="img" aria-label="Aerial photo of a city skyline at dusk with tall towers"></div>
<div class="abs hero-shade"></div>
<div class="abs brand"><span class="brand-square"></span><span class="brand-name">Hollinbrook<br>Counsel</span></div>
<nav class="abs nav"><span class="active">Home</span><span>Services</span><span>Research</span><span>The Institute</span><span>News</span><span>Contact</span></nav>
<div class="abs btn-outline">GET STARTED</div>
<div class="abs hero-frame"></div>
<h1 class="abs serif hero-title">HOLLINBROOK COUNSEL</h1>
<p class="abs hero-sub">Macroeconomic &amp; policy analytics for today's turbulent environment.</p>

<!-- decorative frames -->
<div class="abs line" style="left:-4px;top:616px;width:81px;height:220px"></div>
<div class="abs line" style="left:37px;top:788px;width:73px;height:97px"></div>
<div class="abs line" style="left:1054px;top:608px;width:89px;height:57px"></div>
<div class="abs line" style="left:1080px;top:560px;width:130px;height:75px;border-top:none;border-right:none"></div>

<!-- who we are -->
<h2 class="abs h2" style="top:616px">WHO WE ARE</h2>
<p class="abs para center" style="left:160px;top:672px;width:880px">Lorem ipsum dolor sit amet, consectetur adipiscing elit, sed do eiusmod tempor incididunt ut labore et dolore magna aliqua. Ut enim<br>ad minim veniam, quis nostrud exercitation ullamco laboris nisi ut aliquip ex ea commodo consequat. Duis aute irure dolor in reprehenderit in<br>voluptate velit esse cillum dolore eu fugiat nulla pariatur. Excepteur sint occaecat cupidatat non proident,<br>sunt in culpa qui officia deserunt mollit anim id est laborum.</p>
<div class="abs btn-rose" style="left:534px;top:798px">LEARN MORE</div>

<!-- feature one -->
<div class="photo" style="left:144px;top:913px;width:406px;height:342px;background:linear-gradient(135deg,#c9c2bb,#e8e6e2 45%,#7d8a96)" role="img" aria-label="Photo of a team meeting with a presenter at a flip chart"></div>
<div class="abs" style="left:514px;top:1173px;width:172px;height:172px;border:3px solid rgba(230,230,230,.7)"></div>
<h3 class="abs feature-title" style="left:620px;top:972px;width:450px">SOPHISTICATED RESEARCH &amp; ATYPICAL ANALYSES FOR IMPROVED COMMUNICATIONS.</h3>
<p class="abs para" style="left:619px;top:1094px;width:440px">Lorem ipsum dolor sit amet, consectetur adipiscing elit, sed do<br>eiusmod tempor incididunt ut labore et dolore magna aliqua.<br>enim ad minim veniam, quis nostrud exercitation.</p>
<svg class="abs" style="left:1110px;top:1028px" width="40" height="104" viewBox="0 0 40 104"><g fill="#ebebeb"><path d="M2 2 L20 18 L38 2 L20 44Z"/><path d="M8 50 L20 60 L32 50 L20 76Z"/><path d="M14 82 L20 88 L26 82 L20 100Z"/></g></svg>

<!-- feature two -->
<div class="abs" style="left:790px;top:1350px;width:291px;height:303px;background:var(--rose)"></div>
<div class="photo" style="left:648px;top:1287px;width:407px;height:343px;background:linear-gradient(135deg,#b9c6cf,#e4e4e0 50%,#8b7a6d)" role="img" aria-label="Photo of colleagues discussing charts around an office table"></div>
<h3 class="abs feature-title" style="left:145px;top:1347px;width:460px">PROPRIETARY PUBLIC RELATIONS TOOLS THAT GUARANTEE MEDIA VISIBILITY.</h3>
<p class="abs para" style="left:145px;top:1469px;width:460px">Lorem ipsum dolor sit amet, consectetur adipiscing elit, sed do<br>eiusmod tempor incididunt ut labore et dolore magna aliqua.<br>Ut enim ad minim veniam, quis nostrud exercitation.</p>
<svg class="abs" style="left:55px;top:1403px" width="40" height="104" viewBox="0 0 40 104"><g fill="#ebebeb"><path d="M2 2 L20 18 L38 2 L20 44Z"/><path d="M8 50 L20 60 L32 50 L20 76Z"/><path d="M14 82 L20 88 L26 82 L20 100Z"/></g></svg>

<!-- services -->
<section class="abs services">
  <h2 class="abs h2" style="top:52px">OUR SERVICES</h2>
  <div class="abs service" style="left:113px;top:126px">
    <svg width="90" height="90" viewBox="0 0 90 90" fill="none" stroke="#111" stroke-width="3"><path d="M4 86 H86"/><rect x="10" y="58" width="10" height="26"/><rect x="28" y="46" width="10" height="38"/><rect x="46" y="52" width="10" height="32"/><rect x="64" y="30" width="10" height="54"/><path d="M12 34 L32 20 L50 30 L78 8"/><circle cx="12" cy="34" r="3"/><circle cx="32" cy="20" r="3"/><circle cx="50" cy="30" r="3"/><circle cx="78" cy="8" r="3"/></svg>
    Analytics &amp; Messaging
  </div>
  <div class="abs service" style="left:480px;top:126px">
    <svg width="90" height="90" viewBox="0 0 90 90" fill="none" stroke="#111" stroke-width="3"><path d="M38 4 H52 L54 14 L62 18 L71 12 L80 21 L74 30 L78 38 L86 40 V52 L78 54 L74 62 L80 71 L71 80 L62 74 L54 78 L52 86 H38 L36 78 L28 74 L19 80 L10 71 L16 62 L12 54 L4 52 V40 L12 38 L16 30 L10 21 L19 12 L28 18 L36 14Z"/><circle cx="45" cy="45" r="20"/><path d="M36 40 L56 64 L62 58 L42 36"/><path d="M34 30 A10 10 0 0 0 42 36"/></svg>
    Customized Reports
  </div>
  <div class="abs service" style="left:859px;top:126px">
    <svg width="90" height="90" viewBox="0 0 90 90" fill="none" stroke="#111" stroke-width="3"><path d="M64 30 V86 H6 V4 H50 L64 18"/><rect x="14" y="20" width="12" height="10"/><rect x="14" y="40" width="12" height="10"/><rect x="14" y="60" width="12" height="10"/><path d="M32 25 H46 M32 45 H44 M32 65 H40"/><path d="M46 72 L50 60 L80 30 L86 36 L56 66Z"/></svg>
    Proprietary Surveys
  </div>
  <div class="abs btn-dark" style="left:534px;top:302px">LEARN MORE</div>
</section>

<!-- news -->
<h2 class="abs h2" style="top:2192px">NEWS</h2>
<div class="abs line" style="left:15px;top:2319px;width:111px;height:219px"></div>
<div class="abs line" style="left:1128px;top:2229px;width:80px;height:109px"></div>
<div class="abs line" style="left:1165px;top:2310px;width:40px;height:109px"></div>
<article class="abs card" style="left:144px;top:2259px"><div class="thumb" role="img" aria-label="Photo of capsules spilling from a pill bottle" style="background:linear-gradient(135deg,#c9862e,#5a3a4a 60%,#2c2a2c)"></div><h3>The Tidewater Ledger</h3><a>Read More</a></article>
<article class="abs card" style="left:376px;top:2259px"><div class="thumb" role="img" aria-label="Photo of a coastal city waterfront" style="background:linear-gradient(180deg,#4f9fe0,#e8e0d6 50%,#1c5fa5)"></div><h3>Coastal Health Bulletin News</h3><a>Read More</a></article>
<article class="abs card" style="left:607px;top:2259px"><div class="thumb" role="img" aria-label="Image of a medical technology digital interface" style="background:linear-gradient(135deg,#1d3950,#6aa6c4 55%,#cfe1ea)"></div><h3>Diagnostic Imaging Report</h3><a>Read More</a></article>
<article class="abs card" style="left:839px;top:2259px"><div class="thumb" role="img" aria-label="Photo of lab workers in protective gear" style="background:linear-gradient(135deg,#9bb3c4,#e9ecef 55%,#6b7d88)"></div><h3>Medical Supply Sourcing Journal</h3><a>Read More</a></article>

<!-- footer -->
<footer class="abs footer">
  <div class="abs" style="left:145px;top:52px;width:106px;height:106px;border:3px solid #c98f94;background:var(--white);display:flex;align-items:center;justify-content:center;text-align:center;font-family:'Cinzel',Georgia,serif;font-size:13px;line-height:18px;color:#111">HOLLIN&#8203;BROOK<br>COUNSEL</div>
  <div class="abs" style="left:415px;top:58px;font-size:16px">Questions?</div>
  <div class="abs footer-links" style="left:415px;top:88px">Contact Us</div>
  <div class="abs" style="left:415px;top:122px;width:26px;height:26px;border-radius:50%;background:var(--rose)"></div>
  <div class="abs footer-links" style="left:686px;top:56px">Home<br>Services<br>Research</div>
  <div class="abs footer-links" style="left:973px;top:56px">The Institute<br>In the News<br>Get Started</div>
</footer>
<p class="abs copy">Copyrights © HollinbrookCounsel. 2024 | Allrights Reserved</p>

</body>
</html>
```